Business Card for Nail Art business
Gloss Haven (Card to be non-standard sized)
Business Card for Nail Art business -
Creative Brief
Bright & Fun-filled
Marisa Quell
Ms.
Brimwood Vale and Ashcombe
marisaqv@postlark.net
The business card is to be NON-standard sized, double sided I would wish it to be either 90x45mm or 80x45mm, however it is up to you to find a size that fits your design best, but it must be smaller than standard Please incorporate the logo Feel free to use any font that fits you Please tell me the dimensions of your design/s
The back should have the logo as the main focus, whereas the front should just hold the general contact details, etc. Be creative and see where it goes as even myself is unsure of what I exactly want Feel free to PM me if any questions

```html
<!DOCTYPE html>
<html lang="en">
<head>
<meta charset="utf-8">
<title>Gloss Haven – Business Cards</title>
<link rel="stylesheet" href="https://fonts.googleapis.com/css2?family=Open+Sans:ital,wght@0,600;1,700&family=PT+Serif&display=swap">
<style>
  :root {
    --bg: #ecebea;
    --card: #ffffff;
    --red: #d6181f;
    --red-dark: #a80f14;
    --ink: #1b1b1b;
    --muted: #3a3a3a;
    --rule: #cfcfcf;
  }
  * { box-sizing: border-box; margin: 0; padding: 0; }
  html, body { width: 1200px; height: 852px; overflow: hidden; }
  body { background: var(--bg); position: relative; font-family: "PT Serif", serif; }

  .card {
    position: absolute;
    width: 480px; height: 270px;
    background: var(--card);
    border-radius: 14px;
    overflow: hidden;
    box-shadow: 0 4px 14px rgba(0,0,0,.18);
  }
  .card--contact { left: 90px; top: 150px; }
  .card--feature { left: 630px; top: 432px; }

  .card__bands { position: absolute; inset: 0; width: 100%; height: 100%; }

  .brand { position: absolute; display: flex; align-items: center; gap: 10px; }
  .brand__dot { width: 52px; height: 52px; border-radius: 50%; background: var(--red); flex: none; }
  .brand__name {
    font-family: "Open Sans", sans-serif; font-weight: 600;
    font-size: 28px; color: var(--ink); letter-spacing: .5px; text-transform: uppercase;
    white-space: nowrap;
  }

  .card--contact .brand { left: 48px; top: 112px; gap: 8px; }
  .card--contact .brand__dot { width: 44px; height: 44px; }
  .card--contact .brand__name { font-size: 19px; letter-spacing: .3px; }
  .card--contact .divider {
    position: absolute; left: 262px; top: 66px; width: 1px; height: 140px; background: var(--rule);
  }
  .card--contact .person { position: absolute; left: 278px; top: 78px; }
  .card--contact .contacts { position: absolute; left: 278px; top: 150px; }

  .person__name {
    font-family: "Open Sans", sans-serif; font-style: italic; font-weight: 700;
    font-size: 17px; color: var(--red); white-space: nowrap;
  }
  .person__area { font-size: 12px; color: var(--muted); margin-top: 4px; white-space: nowrap; }

  .contacts { list-style: none; }
  .contacts__item { display: flex; align-items: center; gap: 7px; font-size: 12.5px; color: var(--muted); line-height: 1.9; white-space: nowrap; }
  .contacts__icon { width: 13px; height: 13px; flex: none; }
  .contacts__at { color: var(--red); font-weight: bold; font-size: 14px; width: 13px; text-align: center; }

  .card--feature .brand { left: 92px; top: 52px; }
  .card--feature .brand__dot { width: 66px; height: 66px; }
  .card--feature .person { position: absolute; left: 60px; top: 184px; }
  .card--feature .person__area { font-size: 11.5px; }
  .card--feature .divider {
    position: absolute; left: 218px; top: 178px; width: 1px; height: 56px; background: var(--rule);
  }
  .card--feature .contacts { position: absolute; left: 230px; top: 180px; }
  .card--feature .contacts__item { font-size: 11.5px; }
</style>
</head>
<body>

<section class="card card--contact" aria-label="Gloss Haven contact card">
  <svg class="card__bands" viewBox="0 0 480 270" aria-hidden="true">
    <path d="M0 50 Q30 150 78 270 L0 270 Z" fill="var(--red)"/>
    <path d="M0 70 Q40 170 96 270" fill="none" stroke="var(--ink)" stroke-width="5"/>
    <path d="M480 0 L418 0 Q462 100 480 210 Z" fill="var(--red)"/>
    <path d="M404 0 Q452 104 480 228" fill="none" stroke="var(--ink)" stroke-width="5"/>
  </svg>
  <div class="brand">
    <span class="brand__dot"></span>
    <span class="brand__name">Gloss Haven</span>
  </div>
  <div class="divider"></div>
  <div class="person">
    <p class="person__name">Ms.Marisa Quell</p>
    <p class="person__area">Brimwood Vale &amp; Ashcombe</p>
  </div>
  <ul class="contacts">
    <li class="contacts__item">
      <svg class="contacts__icon" viewBox="0 0 13 13" aria-hidden="true"><rect x="3" y="0.5" width="7" height="12" rx="1.5" fill="none" stroke="var(--red)" stroke-width="1.4"/><rect x="4.6" y="2.2" width="3.8" height="5.5" fill="var(--red)"/></svg>
      <span>0428716453</span>
    </li>
    <li class="contacts__item"><span class="contacts__at">@</span><span>marisaqv@postlark.net</span></li>
  </ul>
</section>

<section class="card card--feature" aria-label="Gloss Haven brand card">
  <svg class="card__bands" viewBox="0 0 480 270" aria-hidden="true">
    <path d="M0 0 L46 0 Q14 30 0 76 Z" fill="var(--red)"/>
    <path d="M440 0 Q404 135 446 270 L480 270 L480 0 Z" fill="var(--red)"/>
    <path d="M428 0 Q390 135 432 270" fill="none" stroke="var(--ink)" stroke-width="5"/>
  </svg>
  <div class="brand">
    <span class="brand__dot"></span>
    <span class="brand__name">Gloss Haven</span>
  </div>
  <div class="person">
    <p class="person__name">Ms.Marisa Quell</p>
    <p class="person__area">Brimwood Vale &amp; Ashcombe</p>
  </div>
  <div class="divider"></div>
  <ul class="contacts">
    <li class="contacts__item">
      <svg class="contacts__icon" viewBox="0 0 13 13" aria-hidden="true"><rect x="3" y="0.5" width="7" height="12" rx="1.5" fill="none" stroke="var(--red)" stroke-width="1.4"/><rect x="4.6" y="2.2" width="3.8" height="5.5" fill="var(--red)"/></svg>
      <span>0428716453</span>
    </li>
    <li class="contacts__item"><span class="contacts__at">@</span><span>marisaqv@postlark.net</span></li>
  </ul>
</section>

</body>
</html>
```